CBD Banner Ad for Print and Zentrix

I we would like a modern European chic that we can use in a 1/4 page ad in our local magazine and also use as our banner ad in the Zentrix ad searches. <br/><br/>We are a high end CBD boutique shop that has their own brand as well as a carefully curated selection of the top end CBD products out on the market. The final design should promote the health and well being that we are trying to live ourselves. We DO NOT want the use of marijuana paraphernalia or like substances. Think Yoga Studio meets Morvik inside of a health store. <br/><br/>Use any images you would like...I have attached a sample product render as well as the inside of our store...but take this in the direction you would like.<br/><br/>The winner will have the added bonus of being able to create 10 more ads for us in the next 6 months.

Target Market(s)

Our target market are the middle to upperclass professional workers that want to take CBD but were afraid due to misinformation or stigma

Font styles to use
Sans Serif

Colors
33b8a4
86cfc6
0792cd
3277b5
85acd3

Requirements
Must have
• A good clean modern design.
• Natural. Organic. Crisp. Welcoming.
Nice to have
• Opal Meadow
• CBD for wellness. CBD for life.
• The font we use for the rest of our campaigns is Adam.
Should not have
• Absolutely NO marijuana leaves, paraphernalia, or references. We are working hard to educate people and get rid of the stigma.

```html
<!DOCTYPE html>
<html lang="en">
<head>
<meta charset="utf-8">
<title>Opal Meadow – Ad Set</title>
<link rel="stylesheet" href="https://fonts.googleapis.com/css2?family=Josefin+Sans:wght@100;200;300&family=Nunito+Sans:wght@400&display=swap">
<style>
  :root {
    --board: #e0e0e0;
    --paper: #fafafa;
    --gold: #b39a5f;
    --gold-button: #bda774;
    --label: #3a3a3a;
    --white: #ffffff;
    --jar-cream: #efe6d2;
    --jar-light: #f6f4ef;
  }
  * { margin: 0; padding: 0; box-sizing: border-box; }
  html, body { width: 1200px; height: 1087px; overflow: hidden; background: var(--board); }
  .board { position: relative; width: 1200px; height: 1087px; }

  .section-title, .size-note {
    position: absolute;
    font-family: "Nunito Sans", sans-serif;
    color: var(--label);
    letter-spacing: 0.3px;
  }
  .section-title { font-size: 26px; top: 148px; }
  .size-note { font-size: 17px; }

  .display { font-family: "Josefin Sans", sans-serif; color: var(--gold); font-weight: 100; }

  /* Print ad */
  .print-ad {
    position: absolute; left: 139px; top: 205px; width: 420px; height: 701px;
    background: var(--paper);
  }
  .print-ad .brand {
    position: absolute; top: 62px; left: 0; width: 100%; text-align: center;
    font-size: 40px; font-weight: 200; letter-spacing: 4px;
  }
  .print-ad .headline {
    position: absolute; top: 184px; left: 0; width: 100%; text-align: center; line-height: 1;
  }
  .print-ad .headline .cbd { display: block; font-size: 66px; letter-spacing: 2px; }
  .print-ad .headline .line { display: block; font-size: 42px; letter-spacing: 3px; margin-top: -4px; }
  .print-ad .product-shot {
    position: absolute; left: 77px; top: 344px; width: 264px; height: 249px;
  }
  .print-ad .url {
    position: absolute; top: 638px; left: 0; width: 100%; text-align: center;
    font-size: 22px; font-weight: 200; letter-spacing: 1px;
  }

  .product-shot { border-radius: 10px; }
  .jar-fill {
    background: radial-gradient(ellipse at 50% 65%, var(--jar-cream) 0%, var(--jar-light) 55%, var(--paper) 100%);
  }

  /* Rectangle web ad */
  .rect-ad {
    position: absolute; left: 631px; top: 205px; width: 202px; height: 168px;
    background: var(--paper);
  }
  .rect-ad .brand { position: absolute; left: 12px; top: 26px; width: 86px; font-size: 17px; font-weight: 200; line-height: 1.1; letter-spacing: 1px; }
  .rect-ad .cbd { position: absolute; left: 12px; top: 76px; font-size: 40px; line-height: 1; }
  .rect-ad .tag { position: absolute; left: 13px; top: 112px; font-size: 7.5px; font-weight: 300; letter-spacing: 0.4px; }
  .rect-ad .product-shot { position: absolute; left: 106px; top: 17px; width: 83px; height: 135px; }
  .rect-ad .cta { left: 13px; top: 130px; width: 85px; height: 21px; font-size: 9px; }

  .cta {
    position: absolute; background: var(--gold-button); color: var(--white);
    font-family: "Nunito Sans", sans-serif; display: flex; align-items: center; justify-content: center;
    letter-spacing: 0.3px;
  }

  /* Leaderboard web ad */
  .leader-ad {
    position: absolute; left: 631px; top: 439px; width: 437px; height: 54px;
    background: var(--paper);
  }
  .leader-ad .brand { position: absolute; left: 20px; top: 13px; width: 74px; font-size: 13px; font-weight: 200; line-height: 1.1; letter-spacing: 1px; text-align: center; }
  .leader-ad .product-shot { position: absolute; left: 99px; top: 8px; width: 98px; height: 38px; border-radius: 4px; }
  .leader-ad .headline { position: absolute; left: 206px; top: 8px; font-size: 13.5px; line-height: 13px; letter-spacing: 0.5px; }
  .leader-ad .cta { left: 325px; top: 16px; width: 85px; height: 24px; font-size: 9px; }
</style>
</head>
<body>
<main class="board">
  <h2 class="section-title" style="left:138px;">LOCAL AD</h2>
  <h2 class="section-title" style="left:629px;">ZENTRIX AD</h2>

  <section class="print-ad">
    <div class="brand display">OPAL MEADOW</div>
    <div class="headline display">
      <span class="cbd">CBD</span>
      <span class="line">FOR WELLNESS</span>
      <span class="line">AND LIFE</span>
    </div>
    <div class="product-shot jar-fill" role="img" aria-label="Product render of three white supplement jars, curcumin softgels in front"></div>
    <div class="url display">WWW.OPALMEADOW.SHOP</div>
  </section>
  <p class="size-note" style="left:138px; top:914px;">15X25CM</p>

  <section class="rect-ad">
    <div class="brand display">OPAL MEADOW</div>
    <div class="cbd display">CBD</div>
    <div class="tag display">FOR WELLNESS &amp; LIFE</div>
    <div class="cta">BUY NOW</div>
    <div class="product-shot jar-fill" role="img" aria-label="Product render of a white curcumin softgel jar"></div>
  </section>
  <p class="size-note" style="left:629px; top:383px;">336X280PX</p>

  <section class="leader-ad">
    <div class="brand display">OPAL MEADOW</div>
    <div class="product-shot jar-fill" role="img" aria-label="Product render of four small supplement jars in a row"></div>
    <div class="headline display">HIGH-END CBD<br>FOR WELLNESS<br>AND LIFE</div>
    <div class="cta">SHOP NOW</div>
  </section>
  <p class="size-note" style="left:629px; top:504px;">728X90PX</p>
</main>
</body>
</html>
```